Need Business Card for our Real Estate Business with Sales Executive's Picture

PANTONE 484 C ( RED)

PANTONE 2766 C ( BLUE

Industry/Entity Type

Real Estate

Contact Information for Business Card

Name, Mobile, email, & picture of Person
Agency Phone, address, Web address

Requirements
Must have
• Our Logo Colours, Agent Picture,

```html
<!DOCTYPE html>
<html lang="en">
<head>
<meta charset="utf-8">
<title>Meridian Real Estate — Business Card</title>
<link href="https://fonts.googleapis.com/css2?family=Cinzel:wght@400;600&family=Open+Sans:wght@400&display=swap" rel="stylesheet">
<style>
  :root {
    --navy: #0c1a42;
    --maroon: #6a0a12;
    --paper: #ffffff;
    --backdrop: #e9e7e4;
    --photo-light: #d9dde6;
    --photo-deep: #23408f;
  }
  html, body {
    margin: 0;
    width: 1200px;
    height: 900px;
    overflow: hidden;
    background: var(--backdrop);
  }
  .canvas { position: relative; width: 1200px; height: 900px; }

  .card {
    position: absolute;
    background: var(--paper);
    overflow: hidden;
    box-shadow: 0 6px 18px rgba(0,0,0,0.18);
  }

  /* Front */
  .card-front { left: 78px; top: 35px; width: 588px; height: 363px; }
  .front-band {
    position: absolute; left: 0; right: 0; top: 182px; bottom: 0;
    background: var(--navy);
  }
  .front-brand {
    position: absolute; left: 30px; top: 62px; width: 300px;
    text-align: center;
    font-family: 'Cinzel', serif; font-weight: 600;
    font-size: 30px; letter-spacing: 2px; line-height: 1.1;
    color: var(--navy);
  }
  .agent-photo {
    position: absolute; left: 312px; top: 0; width: 276px; height: 363px;
    background: linear-gradient(180deg, var(--photo-light) 0%, #8fa0c4 45%, var(--photo-deep) 100%);
  }
  .agent-name {
    position: absolute; left: 30px; top: 206px;
    font-family: 'Cinzel', serif; font-weight: 400;
    font-size: 20px; letter-spacing: 1px; color: var(--paper);
  }
  .contact-list {
    position: absolute; left: 30px; top: 254px;
    margin: 0; padding: 0; list-style: none;
    font-family: 'Open Sans', sans-serif; font-size: 15px;
    color: var(--paper); line-height: 21.5px;
  }
  .contact-list li { display: flex; align-items: center; gap: 8px; }
  .contact-list svg { width: 12px; height: 12px; fill: var(--paper); flex: none; }

  /* Back */
  .card-back { left: 388px; top: 505px; width: 566px; height: 352px; }
  .back-brand {
    position: absolute; left: 0; right: 0; top: 160px;
    text-align: center;
    font-family: 'Cinzel', serif; font-weight: 600;
    font-size: 34px; letter-spacing: 2px;
    color: var(--navy);
  }
  .back-band {
    position: absolute; left: 0; right: 0; bottom: 0; height: 82px;
    background: var(--maroon);
    display: flex; align-items: center; justify-content: center;
    font-family: 'Open Sans', sans-serif; font-size: 15px;
    color: var(--paper);
  }
</style>
</head>
<body>
<main class="canvas">

  <section class="card card-front">
    <div class="front-band"></div>
    <div class="front-brand">Meridian<br>Real Estate</div>
    <div class="agent-photo" role="img" aria-label="Portrait photo of the sales executive in a blue suit"></div>
    <div class="agent-name">Daniel Hart</div>
    <ul class="contact-list">
      <li>
        <svg viewBox="0 0 12 12" aria-hidden="true"><path d="M3 0h6a1 1 0 0 1 1 1v10a1 1 0 0 1-1 1H3a1 1 0 0 1-1-1V1a1 1 0 0 1 1-1zm0 1.5v7.5h6V1.5zM6 10a.6.6 0 1 0 0 1.2A.6.6 0 0 0 6 10z"/></svg>
        044-555 010 220
      </li>
      <li>
        <svg viewBox="0 0 12 12" aria-hidden="true"><path d="M1 3.5C1 2 3 1.5 6 1.5s5 .5 5 2v1H8.5V3.5h-5v1H1zM2.5 6L4 4.8h4L9.5 6v4.5h-7zM6 6.5a1.5 1.5 0 1 0 0 3 1.5 1.5 0 0 0 0-3z"/></svg>
        044-555 010 220
      </li>
      <li>
        <svg viewBox="0 0 12 12" aria-hidden="true"><path d="M0 2.5h12v7H0zM1 3.3v.4l5 3.2 5-3.2v-.4zM1 4.9v3.8h10V4.9L6 8.1z"/></svg>
        hello@meridianhomes.com
      </li>
      <li>
        <svg viewBox="0 0 12 12" aria-hidden="true"><circle cx="6" cy="6" r="5.5"/><path d="M6 .5v11M.5 6h11M3 2c2 1.5 4 1.5 6 0M3 10c2-1.5 4-1.5 6 0" stroke="#0c1a42" stroke-width=".8" fill="none"/></svg>
        www.meridianhomes.com
      </li>
    </ul>
  </section>

  <section class="card card-back">
    <div class="back-brand">Meridian Real Estate</div>
    <div class="back-band">12345, Address Goes Here Country Name, 123456.</div>
  </section>

</main>
</body>
</html>
```